Brisken. business card

We need a business card design for a new mobile car-wash catered toward urban residents. The use of colour should be black, white and red and should be sleek and minimal. The final design should be modern and enticing to look at. A picture of the logo is attached. The font and design should resemble something similar to the logo.

```html
<!DOCTYPE html>
<html lang="en">
<head>
<meta charset="utf-8">
<title>Brisken. business card</title>
<link rel="stylesheet" href="https://fonts.googleapis.com/css2?family=Mulish:wght@400;700&display=swap">
<style>
  :root {
    --backdrop: #d9d9d9;
    --paper: #ffffff;
    --paper-shade: #ececec;
    --ink: #1a1a1a;
    --ink-soft: #555555;
    --brand-red: #e4151f;
    --night: #0b0b0b;
    --night-soft: #1c1c1c;
  }
  * { box-sizing: border-box; margin: 0; padding: 0; }
  html, body { width: 1200px; height: 871px; overflow: hidden; }
  body {
    background: var(--backdrop);
    font-family: "Mulish", sans-serif;
    display: flex;
    flex-direction: column;
    align-items: center;
    justify-content: center;
    gap: 56px;
  }
  .card {
    position: relative;
    width: 620px;
    height: 354px;
    overflow: hidden;
    box-shadow: 0 10px 28px rgba(0,0,0,0.25);
  }

  /* Front */
  .card--front {
    background: linear-gradient(115deg, var(--paper) 45%, var(--paper-shade) 100%);
  }
  .brand-mark {
    position: absolute;
    left: 58px;
    top: 140px;
    width: 250px;
    display: flex;
    flex-direction: column;
    align-items: center;
  }
  .brand-name {
    font-family: "Mulish", sans-serif;
    font-weight: 700;
    font-size: 44px;
    letter-spacing: 4px;
    color: var(--brand-red);
    line-height: 1;
  }
  .brand-rule {
    margin-top: 8px;
    width: 100%;
    height: 1px;
    background: var(--ink-soft);
  }
  .person {
    position: absolute;
    left: 372px;
    top: 92px;
  }
  .person-name {
    font-weight: 700;
    font-size: 19px;
    color: var(--brand-red);
  }
  .person-role {
    font-size: 14px;
    color: var(--ink-soft);
    margin-top: 4px;
  }
  .contact-list {
    position: absolute;
    left: 372px;
    top: 170px;
    list-style: none;
  }
  .contact-item {
    display: flex;
    align-items: center;
    height: 23px;
    font-size: 15px;
    color: var(--ink);
  }
  .contact-icon {
    width: 12px;
    height: 12px;
    margin-right: 26px;
    fill: var(--brand-red);
  }
  .contact-item--email .contact-icon { margin-right: 12px; }
  .edge-band {
    position: absolute;
    left: 0;
    right: 0;
    bottom: 52px;
    height: 16px;
    background: linear-gradient(90deg, var(--ink) 0%, var(--ink) 70%, rgba(26,26,26,0) 100%);
  }
  .edge-accent {
    position: absolute;
    left: 0;
    bottom: 58px;
    width: 66px;
    height: 16px;
    background: var(--brand-red);
  }

  /* Back */
  .card--back {
    background: radial-gradient(ellipse at 50% 40%, var(--night-soft) 0%, var(--night) 75%);
    display: flex;
    flex-direction: column;
    align-items: center;
    justify-content: center;
  }
  .card--back .brand-name { font-size: 50px; }
  .card--back .brand-rule { width: 270px; background: #888888; }
  .website {
    margin-top: 16px;
    font-size: 16px;
    color: #bdbdbd;
    letter-spacing: 0.5px;
  }
  .website-domain { color: var(--brand-red); }
</style>
</head>
<body>

  <section class="card card--front">
    <div class="brand-mark">
      <span class="brand-name">Brisken.</span>
      <span class="brand-rule"></span>
    </div>

    <div class="person">
      <p class="person-name">Marco L Reyes</p>
      <p class="person-role">Ceo</p>
    </div>

    <ul class="contact-list">
      <li class="contact-item">
        <svg class="contact-icon" viewBox="0 0 12 12" aria-hidden="true"><path d="M1 4 Q6 0 11 4 L9 5.5 L8 4 Q6 3.2 4 4 L3 5.5 Z M2.5 7 H9.5 V11 H2.5 Z"/></svg>
        22 641 3907
      </li>
      <li class="contact-item">
        <svg class="contact-icon" viewBox="0 0 12 12" aria-hidden="true"><path d="M3 3 H9 V11 H3 Z M5 0 H7 V3 H5 Z"/></svg>
        91 572 2648
      </li>
      <li class="contact-item">
        <svg class="contact-icon" viewBox="0 0 12 12" aria-hidden="true"><path d="M3.5 0.5 H8.5 V11.5 H3.5 Z M4.5 2 V8 H7.5 V2 Z"/></svg>
        22 641 3950
      </li>
      <li class="contact-item contact-item--email">
        <svg class="contact-icon" viewBox="0 0 12 12" aria-hidden="true"><path d="M0.5 2.5 H11.5 V9.5 H0.5 Z M1.5 3.5 L6 7 L10.5 3.5 Z" fill-rule="evenodd"/></svg>
        marcoreyes@mailbox.com
      </li>
    </ul>

    <div class="edge-band"></div>
    <div class="edge-accent"></div>
  </section>

  <section class="card card--back">
    <span class="brand-name">Brisken.</span>
    <span class="brand-rule"></span>
    <p class="website">www.<span class="website-domain">brisken.com</span></p>
  </section>

</body>
</html>
```